Letterhead for 3 attorney Workers' Comp law firm

We are a 3 attorney law office. We specialize in Workers' Compensation. Our office represents workers who are injured on the job, and the estates of workers who are killed one the job.
When we started our office, we created our own letterhead & have been using it for years. We've just recently hired the 3rd attorney, and were going to just add his name to the letterhead, but have decided we wanted to get a professionally designed letterhead and business cards at this point.
We want something that looks clean and professional. It must look good in black and white because we often make multiple copies of our documents. We're hoping for a design that resonates confidence, reliability and experience.
The design must include the firm name: Dorrance & Pike, PLLC. We would like the PLLC to be small compared to the Dorrance & Pike graphic. We also want to incorporate the attorney names: Ulric Dorrance, Janet Pike, and Lyle Hagberg. Our current letterhead has our contact info in the footer at the bottom of the page. We like that design, but are open to the idea of having it at the top. We'll leave that at the discretion of the designer. Our contact info is as follows: 472 S. Larchmont Avenue, Suite 315 Bellingham, WA 98117 Phone: 360-514-2967, Fax: 360-521-6079, and our website: www.dorrancepike-law.example
Target Market(s)
Clients, courts, other legal offices, doctors offices. These are the people who see our letterhead most frequently. It's not so much for marketing purposes, mainly so that we have a professional image when sending out documents.
Industry/Entity Type
Law Firm
Contact Information for Business Card
On the back of the business card: it can be designed, or be a template for filling in appointment reminder information (i.e. date, time, etc)
Colors
Designer to choose colors to be used in the design.
Requirements
Must have
- Must have our firm name at the top.
- Must include the attorney names.
- Must have all of our contact information (can be at top or bottom - whatever looks best with the design)
Nice to have
- A strong, confident design
Should not have
- We don't want the design to be playful, cartoony or busy.

```html
<!DOCTYPE html>
<html lang="en">
<head>
<meta charset="utf-8">
<title>Dorrance &amp; Pike, PLLC — Letterhead and Business Cards</title>
<link href="https://fonts.googleapis.com/css2?family=Arimo:wght@400;700&display=swap" rel="stylesheet">
<style>
  :root {
    --stage: #4a4a4a;
    --paper: #ffffff;
    --ink: #1a1a1a;
    --brown-dark: #6c3b1f;
    --brown-mid: #8f5230;
    --brown-light: #c1806b;
    --cream: #f3e6de;
    --edge: #8a5a3c;
  }
  * { box-sizing: border-box; margin: 0; padding: 0; }
  html, body {
    width: 1200px; height: 900px; overflow: hidden;
    background: var(--stage);
    font-family: "Arimo", Arial, sans-serif;
  }
  .canvas { position: relative; width: 1200px; height: 900px; }

  .corner-ornament { position: absolute; top: 0; right: 0; }

  /* Letterhead */
  .letterhead {
    position: absolute; left: 70px; top: 60px;
    width: 600px; height: 776px;
    background: var(--paper);
  }
  .letterhead .corner-ornament {
    width: 290px; height: 200px;
    background: linear-gradient(200deg, var(--brown-dark) 0%, var(--brown-mid) 55%, var(--brown-light) 100%);
  }
  .firm-name { color: var(--ink); font-weight: 400; line-height: 1.05; }
  .firm-name .pllc { display: block; }
  .letterhead .firm-name {
    position: absolute; left: 60px; top: 130px; width: 200px;
    font-size: 34px; text-align: center;
  }
  .letterhead .firm-name .pllc { font-size: 16px; letter-spacing: 2px; margin-top: 4px; }
  .attorneys { text-align: center; }
  .attorneys .label { font-size: 10px; color: var(--ink); margin-bottom: 4px; }
  .attorneys .name { font-weight: 700; color: var(--brown-dark); }
  .letterhead .attorneys { position: absolute; left: 60px; top: 300px; width: 200px; }
  .letterhead .attorneys .name { font-size: 12px; line-height: 21px; }
  .letterhead .contact {
    position: absolute; left: 180px; bottom: 60px; width: 220px;
    text-align: center; font-size: 10px; line-height: 18px; color: var(--ink);
    font-style: normal;
  }

  /* Business cards */
  .card { position: absolute; width: 400px; height: 222px; overflow: hidden; }
  .card .corner-ornament { width: 195px; height: 92px; }
  .card-front { left: 720px; top: 270px; background: var(--brown-dark); }
  .card-front .corner-ornament {
    background: linear-gradient(200deg, var(--paper) 0%, var(--cream) 100%);
  }
  .card-front .firm-name {
    position: absolute; left: 20px; top: 62px; width: 200px;
    text-align: center; font-size: 30px; color: var(--paper);
  }
  .card-front .firm-name .pllc { font-size: 14px; letter-spacing: 2px; margin-top: 3px; }
  .card-back {
    left: 780px; top: 460px; background: var(--paper);
    border: 1px solid var(--edge);
  }
  .card-back .corner-ornament {
    background: linear-gradient(200deg, var(--brown-dark) 0%, var(--brown-mid) 55%, var(--brown-light) 100%);
  }
  .card-back .attorneys { position: absolute; left: 30px; top: 40px; width: 140px; }
  .card-back .attorneys .name { font-size: 15px; line-height: 28px; }
  .card-back .contact {
    position: absolute; right: 12px; bottom: 24px;
    text-align: right; font-size: 9.5px; line-height: 15px; color: #333;
    font-style: normal;
  }
</style>
</head>
<body>
<main class="canvas">

  <section class="letterhead" aria-label="Letterhead">
    <div class="corner-ornament" role="img" aria-label="Corner ornament of angled brown bands"></div>
    <h1 class="firm-name">Dorrance<br>&amp;<br>Pike<span class="pllc">PLLC</span></h1>
    <div class="attorneys">
      <p class="label">Attorneys :</p>
      <p class="name">Ulric Dorrance</p>
      <p class="name">Janet Pike</p>
      <p class="name">Lyle Hagberg</p>
    </div>
    <address class="contact">
      472 S. Larchmont Avenue,<br>
      Suite 315 Bellingham,<br>
      WA 98117<br>
      Phone: 360-514-2967,<br>
      Fax: 360-521-6079<br>
      www.dorrancepike-law.example
    </address>
  </section>

  <section class="card card-front" aria-label="Business card front">
    <div class="corner-ornament" role="img" aria-label="Corner ornament of angled white bands"></div>
    <h2 class="firm-name">Dorrance<br>&amp;<br>Pike<span class="pllc">PLLC</span></h2>
  </section>

  <section class="card card-back" aria-label="Business card back">
    <div class="corner-ornament" role="img" aria-label="Corner ornament of angled brown bands"></div>
    <div class="attorneys">
      <p class="label">Attorneys :</p>
      <p class="name">Ulric Dorrance</p>
      <p class="name">Janet Pike</p>
      <p class="name">Lyle Hagberg</p>
    </div>
    <address class="contact">
      472 S. Larchmont Avenue, Suite 315 Bellingham, WA 98117<br>
      Phone: 360-514-2967, Fax: 360-521-6079<br>
      website: www.dorrancepike-law.example
    </address>
  </section>

</main>
</body>
</html>
```